tolv Marketing Brochure for construction of multi-million dollar homes in the Caribbean

Design a marketing brochure for a construction company operating in the Caribbean for ultra high-end signature homes and villas. Target audience is ultra high net worth individuals, families, international property developers and hotel chains. We have provided an our marketing brochure for reference but would like a totally new look and feel with updated wording and photos (also provided). The company logo of light and dark blue circles and 'tolv' with the 's' in superscript must feature throughout. Further information can be extracted from the company's website: tolvharbour.example. Depending on how this goes there may be additional projects such as website and log redesign. Thanks!

Target Market(s)

Target audience is ultra high net worth individuals, families, international property developers and hotel chains.

Font styles to use
Other font styles liked:
• see logo for desired phones

Colors
3aa7d7
0655a3
85cae6
3176b5
85acd3
33a6d7
cee9f5
cedeed

Requirements
Must have
• Detailed company info including projects and employee profiles - must be bold, brilliant and eye-catching.
Nice to have
• Colour
Should not have
• Too much info.

```html
<!DOCTYPE html>
<html lang="en">
<head>
<meta charset="utf-8">
<title>tolv — Brochure Spreads</title>
<link href="https://fonts.googleapis.com/css2?family=Lato:wght@300;400;700&family=Montserrat:wght@500;800&family=Roboto+Condensed:wght@400&display=swap" rel="stylesheet">
<style>
  :root{
    --stage:#c5d9dc;
    --paper:#ffffff;
    --navy:#0b3f95;
    --royal:#0655a3;
    --band:#1f63ae;
    --sky:#3aa7d7;
    --mist:#85cae6;
    --ink:#3a3a3a;
    --grey:#6b6b6b;
    --logo-grey:#5d5a58;
  }
  *{box-sizing:border-box;margin:0;padding:0}
  html,body{width:1200px;height:1200px;overflow:hidden;background:var(--stage)}
  body{position:relative;font-family:"Lato",sans-serif;color:var(--ink)}
  .page{position:absolute;width:511px;height:364px;background:var(--paper);overflow:hidden;box-shadow:5px 5px 6px rgba(0,0,0,.45)}
  .p-cover{left:40px;top:16px}
  .p-welcome{left:647px;top:16px}
  .p-services{left:40px;top:418px}
  .p-network{left:647px;top:418px}
  .p-report{left:40px;top:820px}
  .p-back{left:647px;top:820px}

  .photo{position:absolute}
  .photo-entrance{left:0;top:77px;width:511px;height:244px;
    background:
      radial-gradient(ellipse 30% 55% at 50% 58%, #7a3d1c 0%, rgba(122,61,28,0) 100%),
      radial-gradient(ellipse 45% 40% at 50% 38%, #c96a26 0%, rgba(201,106,38,0) 100%),
      radial-gradient(ellipse 25% 45% at 8% 70%, #3f6b26 0%, rgba(63,107,38,0) 100%),
      radial-gradient(ellipse 25% 45% at 92% 70%, #4d7e2c 0%, rgba(77,126,44,0) 100%),
      linear-gradient(180deg,#3f86d6 0%,#8cc0ec 22%,#c98a4e 45%,#8a6a3e 68%,#5f8a36 84%,#d9d2c4 100%)}
  .photo-headland{left:0;top:0;width:359px;height:364px;
    background:
      radial-gradient(ellipse 40% 18% at 82% 38%, rgba(255,255,255,.85) 0%, rgba(255,255,255,0) 100%),
      radial-gradient(ellipse 70% 16% at 55% 57%, #8c7a5c 0%, rgba(140,122,92,0) 100%),
      linear-gradient(180deg,#0d46ad 0%,#2c6fd0 22%,#7fb3e6 36%,#9c8a68 48%,#7c6a4e 62%,#1b5fae 72%,#0c4fa0 86%,#093e8c 100%)}
  .photo-aerial{left:0;top:0;width:511px;height:222px;
    background:
      radial-gradient(ellipse 18% 14% at 80% 68%, #2fc0ee 0%, rgba(47,192,238,0) 100%),
      radial-gradient(ellipse 28% 22% at 62% 58%, #eef1f2 0%, rgba(238,241,242,0) 100%),
      radial-gradient(ellipse 40% 35% at 48% 42%, #6e6663 0%, rgba(110,102,99,0) 100%),
      linear-gradient(135deg,#4e6e36 0%,#5d7440 30%,#6a6a60 50%,#556f3a 75%,#3f6b2e 100%)}
  .photo-pavilion{left:366px;top:172px;width:125px;height:125px;border:2px solid #fff;box-shadow:0 0 0 1px #ddd;
    background:linear-gradient(180deg,#b5582a 0%,#d6946a 30%,#f4f2ee 42%,#8fd0ec 55%,#d8d2c8 70%,#7a5a44 100%)}
  .photo-greenroof{left:0;top:0;width:511px;height:364px;
    background:
      radial-gradient(ellipse 30% 30% at 25% 70%, #9a7256 0%, rgba(154,114,86,0) 100%),
      radial-gradient(ellipse 35% 20% at 30% 38%, #7c8a44 0%, rgba(124,138,68,0) 100%),
      radial-gradient(ellipse 25% 40% at 88% 75%, #4f7a2a 0%, rgba(79,122,42,0) 100%),
      linear-gradient(180deg,#a9d3ef 0%,#1858c0 6%,#0f4db6 35%,#1a62b8 55%,#6a7e44 72%,#8a6c4c 88%,#5a7a30 100%)}
  .photo-coast{left:116px;top:0;width:194px;height:48px;background:linear-gradient(180deg,#7fb0e0 0%,#f2f4f6 50%,#8a958c 75%,#5b6d55 100%)}
  .photo-interior{left:318px;top:0;width:193px;height:48px;background:linear-gradient(90deg,#d9c6a6 0%,#efe8dc 45%,#9cc6e4 75%,#4e9ad6 100%)}
  .photo-dusk{left:116px;top:108px;width:395px;height:152px;
    background:
      radial-gradient(ellipse 45% 22% at 50% 48%, #f0b04a 0%, rgba(240,176,74,0) 100%),
      linear-gradient(180deg,#9aaabb 0%,#6a7a88 18%,#4f4a42 36%,#7a5e3a 52%,#5e5040 70%,#4a4036 100%)}
  .photo-gazebo{left:116px;top:266px;width:278px;height:98px;background:linear-gradient(180deg,#b89160 0%,#d4b07e 35%,#8ec6e6 62%,#e8e4dc 82%,#cfc8bc 100%)}
  .photo-basin{left:400px;top:266px;width:111px;height:98px;background:linear-gradient(135deg,#5f7a3e 0%,#a88e70 50%,#5a4a3c 100%)}

  .brand{position:absolute;display:flex;align-items:center;gap:7px;font-family:"Lato",sans-serif;font-weight:300;color:var(--logo-grey);line-height:1}
  .brand .dot{border-radius:50%;background:var(--royal);flex:none}
  .brand.light{color:#fff}
  .brand.light .dot{background:#fff}
  .tagline{font-size:7px;font-family:"Lato",sans-serif;color:var(--grey);margin-left:8px;letter-spacing:.2px}
  .brand.light .tagline{color:rgba(255,255,255,.6);font-size:4px}
  .url{position:absolute;font-size:7px;letter-spacing:2.6px;color:#333}
  .folio{position:absolute;font-size:6px;font-weight:700;color:#222}
  .copy{position:absolute;font-size:5.6px;line-height:1.6;text-align:justify;color:#333}
  .copy .hl{color:var(--royal)}

  .p-cover .brand{left:98px;top:16px;font-size:44px}
  .p-cover .brand .dot{width:36px;height:36px;background:var(--royal)}
  .p-cover .tagline{color:#555}
  .p-cover .url{left:0;right:0;text-align:center;top:341px}

  .welcome-title{position:absolute;left:22px;top:20px;color:#fff}
  .welcome-title h1{font-family:"Montserrat",sans-serif;font-weight:800;font-size:22px;letter-spacing:.3px}
  .welcome-title p{font-family:"Montserrat",sans-serif;font-weight:500;font-size:14px;margin-top:1px}
  .p-welcome .copy{left:369px;top:63px;width:121px}
  .p-welcome .brand{left:22px;top:312px;font-size:22px}
  .p-welcome .brand .dot{width:17px;height:17px}
  .p-welcome .url{left:22px;top:338px;color:#fff;letter-spacing:1px;font-size:6.5px}

  .p-services .copy{left:22px;top:243px;width:274px}
  .p-services .copy p+p{margin-top:8px}
  .p-services .brand{left:22px;top:322px;font-size:22px}
  .p-services .brand .dot{width:16px;height:16px}
  .p-services .tagline{font-size:3.5px;color:#999}

  .p-network .copy{left:304px;top:57px;width:186px;color:#fff}
  .p-network .brand{left:22px;top:305px;font-size:22px}
  .p-network .brand .dot{width:17px;height:17px}
  .p-network .folio{color:#fff}

  .report-band{position:absolute;left:98px;top:50px;width:413px;height:54px;background:var(--band);display:flex;align-items:center;padding-left:11px}
  .report-band h2{font-family:"Roboto Condensed",sans-serif;font-weight:400;font-size:17.5px;color:#fff;letter-spacing:.2px}
  .p-report .copy{left:22px;top:172px;width:73px;font-size:6.3px;line-height:1.35}
  .p-report .brand{left:22px;top:322px;font-size:22px}
  .p-report .brand .dot{width:16px;height:16px}

  .p-back .brand{left:25px;top:316px;font-size:24px}
  .p-back .brand .dot{width:18px;height:18px}
  .p-back .tagline{font-size:5px}
  .contact{position:absolute;top:317px;font-size:5px;color:#333;line-height:2.2}
  .contact div{display:flex;align-items:center;gap:2px}
  .contact svg{width:5px;height:5px}
  .p-back .legal{position:absolute;left:0;right:0;top:338px;text-align:center;font-size:5px;color:#555}
  .p-back .rule{position:absolute;left:0;right:0;bottom:0;height:9px;background:var(--navy)}
</style>
</head>
<body>

<section class="page p-cover">
  <div class="brand"><span class="dot"></span>tolv<span class="tagline">engineering . management. construction</span></div>
  <div class="photo photo-entrance" role="img" aria-label="Timber-framed villa entrance framed by palm trees and tropical gardens"></div>
  <div class="url">www.tolvharbour.example</div>
</section>

<section class="page p-welcome">
  <div class="photo photo-headland" role="img" aria-label="Clifftop villas on a rocky headland above the sea"></div>
  <div class="welcome-title">
    <h1>WELCOME TO tolv...</h1>
    <p>Professionals in building</p>
  </div>
  <p class="copy">If you are looking to build your ultimate dream home in your own piece of paradise, tolv Caribbean Ltd ("tolv") can not only make it a reality, but can do it in a way that is seamless and specifically tailored for you and your needs. tolv covers all aspects of the building process, from conceptual project planning and design, through to completion and everything in between. Specialising in creating luxurious private residences throughout the Caribbean, tolv has built an enviable portfolio of breathtaking villas and opulent homes for extremely satisfied clientele.</p>
  <div class="brand light"><span class="dot"></span>tolv<span class="tagline">engineering . management. construction</span></div>
  <div class="url">www.tolvharbour.example</div>
  <div class="folio" style="left:489px;top:338px">1</div>
</section>

<section class="page p-services">
  <div class="photo photo-aerial" role="img" aria-label="Aerial view of a hillside villa with an infinity pool"></div>
  <div class="photo photo-pavilion" role="img" aria-label="Open living pavilion with timber ceiling looking out to the beach"></div>
  <div class="copy">
    <p><span class="hl">tolv</span> caters to clients who are not able to be present for the duration of their project and therefore require building professionals to represent their best interests. From the beginning of the process, our services will help you understand in detail how we get to the end product with the agreed original parameters.</p>
    <p><span class="hl">Our team</span> consists largely of British and American personnel with support from local communities &amp; consists of Project Managers, Chartered Builders, Civil and Structural Engineers, Chartered Quantity Surveyors, Estimators and Qualified Electrical &amp; Mechanical Engineers.</p>
  </div>
  <div class="brand"><span class="dot"></span>tolv<span class="tagline">engineering . management. construction</span></div>
  <div class="folio" style="left:487px;top:337px">2</div>
</section>

<section class="page p-network">
  <div class="photo photo-greenroof" role="img" aria-label="Stone villa with a planted green roof overlooking the ocean"></div>
  <p class="copy">tolv have an unparalleled network of professional service providers available for any nature of high-end development, having partnered with a diverse range of premium project design teams, architects, engineers and specialist trade contractors. Due to these long and established relationships, tolv is able to provide clients the greatest choice of resources, mobilise at short notice and ensure superior client delivery every time.</p>
  <div class="brand light"><span class="dot"></span>tolv</div>
  <div class="folio" style="left:489px;top:336px">3</div>
</section>

<section class="page p-report">
  <div class="photo photo-coast" role="img" aria-label="Coastal hills under a cloudy sky"></div>
  <div class="photo photo-interior" role="img" aria-label="Bright interior with sea view windows"></div>
  <div class="report-band"><h2>PROJECT INCEPTION REPORT</h2></div>
  <div class="photo photo-dusk" role="img" aria-label="Villa lit up at dusk above stone terrace walls"></div>
  <div class="photo photo-gazebo" role="img" aria-label="Thatched beach gazebo with lounge seating"></div>
  <div class="photo photo-basin" role="img" aria-label="Stone water basin in a garden courtyard"></div>
  <p class="copy">tolv partner intrinsically with the design team through the design and planning phase to ensure that all parameters of the project are clearly defined, understood and adhered to giving clients comfort and peace of mind from the outset.</p>
  <div class="brand"><span class="dot"></span>tolv</div>
  <div class="folio" style="left:488px;top:338px;color:#fff">4</div>
</section>

<section class="page p-back">
  <div class="brand"><span class="dot"></span>tolv<span class="tagline">engineering . management. construction</span></div>
  <div class="contact" style="left:250px">
    <div><svg viewBox="0 0 10 10"><circle cx="5" cy="5" r="4.5" fill="var(--mist)"/></svg>123-456-789-456</div>
    <div><svg viewBox="0 0 10 10"><circle cx="5" cy="5" r="4.5" fill="var(--mist)"/></svg>123-456-789-123</div>
  </div>
  <div class="contact" style="left:335px">
    <div><svg viewBox="0 0 10 10"><circle cx="5" cy="5" r="4.5" fill="var(--mist)"/></svg>www.tolvharbour.example</div>
    <div><svg viewBox="0 0 10 10"><rect x="1" y="2" width="8" height="6" fill="var(--mist)"/></svg>office@tolvharbour.example</div>
  </div>
  <div class="contact" style="left:427px">
    <div><svg viewBox="0 0 10 10"><path d="M5 0a3.5 3.5 0 0 1 3.5 3.5C8.5 6 5 10 5 10S1.5 6 1.5 3.5A3.5 3.5 0 0 1 5 0z" fill="var(--sky)"/></svg>Your office address here</div>
  </div>
  <p class="legal">Copyright © tolv Caribbean 2017. All Rights Reserved.</p>
  <div class="rule"></div>
</section>

</body>
</html>
```